Create a responsive clean and mean platform

We support global forensic investigations (like korvatec or osterlane affair). We help the clients (Chief Legal Officer) to get insights on potential risks to their company and how to act on them. When in need they will immediately call us. we want to create a platform that supports the client in everydaty tasks considering forensic and risks.

Homepage (after login client): This page has following areas:
There should be a standard layout on every page with search, messages, navigation and login name (you see the client is logged in)

1. first area shows different risk and issues related to the company using the platform. There are different types of alerts and issues, like, compliance issues, risk issues, risk alerts, industry alerts and business alerts. You are able to click on the alerts and go into more details. The area of issues gives the option for view between list details or an icon view.
Second area on this page: It's big and show a map in the style provided (see screenshots). The map show an overview of new articles from around the world. The news article related to the client business are plotted on the map. Every time there is a new news feed, you will have a small pop up that shows the feed for 2 seconds top right corner. The map is interactive and also has a timeline in the bottom to slide from a year ago to now.
Third area: Shows a process status of a green eye project. It shows the complete process and the current status.
Fourth area: Shows two overviews of budget Vs. Costs and Planned Vs. Actual. When clicking on them the client goes to a page with more detail.

Search page: We would like a search page that shows the search results of for example Osterlane affair. It contains two different areas. First showing are issues and risk from within the company that are related to "Osterlane affair". With a short description on the issue and that the issue was resolved a week ago. '
Second area: contains news related articles, with header, small picture related to "osterlane affair".

Issue Detail Page: Contains details about the issues and alerts you clicked from the homepage. The details contains to call to action parts: one is to navigate to get in contact for this particular issue. The second part is related document. Apart from that you also see other related issues and alerts.

Get in contact for certain issue/alert page:
Contains contact cards as shown in the style examples. On the left you first see contact card with the title Head Quarter. Contact: Marla Quisdorf with a picture of the contact. Like in the screenshot, except you can push a call button or email button.
Below another contact card in the same style with Regional. Contact: Tobin Welsacre and also you can push a call button or email button.
On the right side you see current subscription that says three things: Prevent, Detect and Repond full platinum subscription
Below just like in the example you see three experts with name photo and expertise.

Any other colors then what we included. Icons and stuff and cool graphics are always welcome.
Please use the screenshots provided as reference for the design style.

Target Market(s)

Client Chief Officer (CLO)

Industry/Entity Type

Security

Number of Pages Required

4 page

Font styles to use
Other font styles liked:
• If possible frutiger or open sans if not Sans serif

Colors
9bcb3c
0555a3
0592cd

Requirements
Must have
• It should be a clean and sterile platform. Which is light from color and uses color to accentuate risk issue's and call to action.
• Please use the following color codes: Dark blue R0 G39 B118, Green R129 G188 B0, blue R0 G161 B222, Light blue R114 G199 B231, Dark green R60 G138 B46, light green R189 G210 B3.
Nice to have
• next to desktop also one page on iphone
Should not have
• It's a side from business to business. So don't be loosley in use of drawn graphics. Icons are welcome ofcourse

```html
<!DOCTYPE html>
<html lang="en">
<head>
<meta charset="utf-8">
<title>Forensic Investigator – Client Dashboard</title>
<link href="https://fonts.googleapis.com/css2?family=Open+Sans:wght@400;600;700&display=swap" rel="stylesheet">
<style>
:root{
  --frame:#e6e6e6;
  --page:#f3f3f3;
  --header:#3c8a2e;
  --header-dark:#2f7424;
  --lime:#a3cd3f;
  --lime-text:#8abf1e;
  --accent:#81bc00;
  --panel:#e9e9e9;
  --row:#e2e2e2;
  --ink:#3d3d3d;
  --muted:#666;
  --btn:#8c8c8c;
  --chev:#6f6f6f;
  --navy:#002776;
  --white:#fff;
}
*{box-sizing:border-box;margin:0;padding:0}
html,body{width:1200px;height:2880px;overflow:hidden}
body{font-family:"Open Sans",Arial,sans-serif;background:var(--frame);color:var(--ink);position:relative}
.canvas{position:absolute;left:15px;top:15px;width:1170px;height:2850px;background:linear-gradient(180deg,#d9d9d9 0,#f4f4f4 190px,var(--page) 400px,#f7f7f7 100%);overflow:hidden}
.abs{position:absolute}
/* header */
.topbar{left:0;top:0;width:1170px;height:100px;background:var(--header)}
.brand{left:25px;top:30px;display:flex;align-items:center;gap:12px;color:var(--white);font-size:21px;font-weight:600}
.brand .mark{width:34px;height:34px;border:2px solid var(--white)}
.tab{top:46px;height:54px;width:158px;background:#e9e9e9;border-radius:4px 4px 0 0;font-size:12px;color:#555;text-align:center;padding-top:6px;text-transform:uppercase}
.tab svg{display:block;margin:0 auto 4px}
.tab.active{background:linear-gradient(180deg,var(--header) 0,#6bab1f 50%,#b9d80c 100%);color:var(--white)}
.user{right:30px;top:38px;display:flex;align-items:center;gap:22px;color:var(--white);font-size:14px;font-weight:600}
.search{left:331px;top:115px;width:508px;height:39px;background:var(--white);border-radius:2px;display:flex;align-items:center;padding:0 12px;gap:14px;font-size:13px;color:#777;box-shadow:0 1px 2px rgba(0,0,0,.15)}
.search .go{margin-left:auto;width:28px;height:26px;background:#8a8a8a;color:var(--white);font-size:9px;display:flex;align-items:center;justify-content:center}
/* sections */
.col{left:135px;width:900px}
.bar{height:58px;background:var(--lime);color:var(--white);font-size:17px;font-weight:600;display:flex;align-items:center;padding:0 42px;text-transform:uppercase}
.bar.company{background:#6fac5e;font-size:20px}
.chev{margin-left:auto;width:20px;height:20px;border-radius:50%;background:var(--chev);display:flex;align-items:center;justify-content:center}
.row{height:48px;background:var(--row);display:flex;align-items:center;padding:0 42px 0 38px;gap:18px;font-size:13px;font-weight:700;color:var(--lime-text);text-transform:uppercase;border-bottom:2px solid #f4f4f4}
.row .ic{width:26px;display:flex;justify-content:center}
.panel{background:var(--panel)}
.btn{background:var(--btn);color:var(--white);font-size:15px;text-transform:uppercase;display:flex;align-items:center;justify-content:center}
.issue h3{font-size:20px;font-weight:600;color:#444}
.issue .date{font-size:14px;font-weight:700;color:#444;margin-top:4px}
.issue p,.copy{font-size:14px;line-height:22px;color:#555}
.company-info{font-size:20px;font-weight:700;color:var(--accent);line-height:26px}
.company-info b{color:#7ab800}
.photo{background:linear-gradient(160deg,#f0f0f0,#2b2b2b 70%,#1a1a1a)}
.map{background:radial-gradient(ellipse at 50% 45%,#c7e37a 0,#dcee b3 0,#d6ea9c 35%,#eef6d8 70%,#f6f6f6 100%)}
.pin{width:26px;height:34px}
.tip{background:#b5d531;color:var(--white);border-radius:6px;padding:8px 10px;font-size:12px;line-height:15px;font-weight:600}
.year{background:var(--white);border:1px solid #cfcfcf;border-radius:16px;display:flex;align-items:center;justify-content:center;gap:26px;font-size:18px;font-weight:600;color:#555}
.timeline{height:2px;background:#c9c9c9}
.dot{width:20px;height:20px;border-radius:50%;border:2px solid #a9cd3a;background:#eaf3cc}
.dot.on{border-color:var(--header);background:#9bc94a}
.month{width:60px;text-align:center;font-size:13px;font-weight:700;color:#555}
.month.on{color:var(--navy);font-size:18px;top:1853px}
.circle{width:130px;height:130px;border-radius:50%;background:var(--white);display:flex;align-items:center;justify-content:center}
.cap{width:240px;text-align:center;font-size:14px;line-height:22px;color:#555}
</style>
</head>
<body>
<div class="canvas">

  <!-- global header -->
  <div class="abs topbar"></div>
  <div class="abs brand"><span class="mark"></span>Forensic Investigator</div>
  <div class="abs tab active" style="left:342px"><svg width="18" height="16" viewBox="0 0 18 16"><path d="M9 1 1 8h2v7h4v-5h4v5h4V8h2z" fill="#fff"/></svg>Home</div>
  <div class="abs tab" style="left:508px"><svg width="16" height="18" viewBox="0 0 16 18"><rect x="1" y="1" width="14" height="16" fill="none" stroke="#555" stroke-width="2"/><path d="M4 6h8M4 9h8M4 12h8" stroke="#555" stroke-width="1.5"/></svg>Issue Detail</div>
  <div class="abs tab" style="left:672px"><svg width="18" height="18" viewBox="0 0 18 18"><path d="M4 1l3 4-2 2c1 2 3 4 5 5l2-2 4 3-2 3C8 16 2 10 1 4z" fill="#555"/></svg>Get in contact</div>
  <div class="abs user">
    <svg width="46" height="28" viewBox="0 0 46 28"><g fill="#7ec8ea"><circle cx="23" cy="8" r="6"/><path d="M12 27c0-8 5-11 11-11s11 3 11 11z"/><circle cx="9" cy="10" r="4.5"/><path d="M0 25c0-6 4-8 9-8 2 0 3 .4 4 1-2 2-3 4-3 7z"/><circle cx="37" cy="10" r="4.5"/><path d="M46 25c0-6-4-8-9-8-2 0-3 .4-4 1 2 2 3 4 3 7z"/></g></svg>
    <span>Welcome Elias Brandvik &#8964;</span>
  </div>
  <div class="abs search">
    <svg width="22" height="22" viewBox="0 0 22 22"><circle cx="12" cy="9" r="7" fill="none" stroke="#444" stroke-width="2.5"/><path d="M7 14 1 20" stroke="#444" stroke-width="3"/></svg>
    SEARCH<span class="go">GO</span>
  </div>

  <!-- company -->
  <div class="abs col bar company" style="top:240px">ABC Corporation</div>
  <div class="abs col panel" style="top:298px;height:182px"></div>
  <div class="abs" style="left:305px;top:340px;width:98px;height:98px;border-radius:50%;border:5px solid var(--accent)"></div>
  <div class="abs company-info" style="left:428px;top:362px">COMPANY: <b>ABC CORPORATION</b><br>CONTACT: <b>CORINNE VALDRE</b></div>
  <div class="abs photo" role="img" aria-label="Portrait photo of the client contact" style="left:769px;top:312px;width:108px;height:168px"></div>

  <!-- risks & issues -->
  <div class="abs col bar" style="top:521px">Risks &amp; Issues<span class="chev"><svg width="10" height="7" viewBox="0 0 10 7"><path d="M1 6 5 2l4 4" fill="none" stroke="#fff" stroke-width="2"/></svg></span></div>
  <div class="abs col row" style="top:580px"><span class="ic"><svg width="22" height="24" viewBox="0 0 22 24"><rect x="2" y="3" width="16" height="19" fill="none" stroke="#8abf1e" stroke-width="2"/><path d="M6 9h8M6 13h8M6 17h5" stroke="#8abf1e" stroke-width="1.6"/><circle cx="17" cy="19" r="4" fill="#8abf1e"/></svg></span>Compliance Issues<span class="chev"><svg width="10" height="7" viewBox="0 0 10 7"><path d="M1 6 5 2l4 4" fill="none" stroke="#fff" stroke-width="2"/></svg></span></div>
  <div class="abs col panel" style="top:630px;height:244px"></div>
  <div class="abs issue" style="left:170px;top:660px;width:840px">
    <div style="position:absolute;left:0;top:0"><svg width="36" height="40" viewBox="0 0 22 24"><rect x="2" y="3" width="16" height="19" fill="none" stroke="#8abf1e" stroke-width="2"/><path d="M6 9h8M6 13h8M6 17h5" stroke="#8abf1e" stroke-width="1.6"/><circle cx="17" cy="19" r="4" fill="#8abf1e"/></svg></div>
    <div style="margin-left:50px">
      <h3>ISSUE #1</h3><div class="date">June 15, 2016</div>
      <p>Lorem ipsum dolor sit amet, consectetuer adipiscing elit, sed diam nonummy nibh euismod tincidunt ut laoreet dolore magna aliquam erat volutpat. Ut wisi enim ad minim veniam, quis nostrud exerci tation ullamcorper sus cipit lobortis nisl ut aliquip ex ea commodo consequat. Duis autem vel eum iriure dolor in hendrerit in vulputate velit esse molestie consequat.</p>
    </div>
  </div>
  <div class="abs btn" style="left:905px;top:835px;width:130px;height:39px">View Details</div>
  <div class="abs col panel" style="top:876px;height:113px;background:#e5e5e5"></div>
  <div class="abs issue" style="left:170px;top:905px;width:840px">
    <div style="position:absolute;left:0;top:0"><svg width="36" height="40" viewBox="0 0 22 24"><rect x="2" y="3" width="16" height="19" fill="none" stroke="#8abf1e" stroke-width="2"/><path d="M6 9h8M6 13h8M6 17h5" stroke="#8abf1e" stroke-width="1.6"/><circle cx="17" cy="19" r="4" fill="#8abf1e"/></svg></div>
    <div style="margin-left:50px"><h3>ISSUE #2</h3><div class="date">June 12, 2016</div></div>
  </div>
  <div class="abs chev" style="left:993px;top:932px"><svg width="10" height="7" viewBox="0 0 10 7"><path d="M1 1l4 4 4-4" fill="none" stroke="#fff" stroke-width="2"/></svg></div>
  <div class="abs col row" style="top:991px"><span class="ic"><svg width="6" height="24" viewBox="0 0 6 24"><rect x="1" y="0" width="4" height="16" fill="#8abf1e"/><rect x="1" y="19" width="4" height="4" fill="#8abf1e"/></svg></span>Risk Issues<span class="chev"><svg width="10" height="7" viewBox="0 0 10 7"><path d="M1 1l4 4 4-4" fill="none" stroke="#fff" stroke-width="2"/></svg></span></div>
  <div class="abs col row" style="top:1041px"><span class="ic"><svg width="26" height="22" viewBox="0 0 26 22"><circle cx="13" cy="11" r="7" fill="none" stroke="#8abf1e" stroke-width="2.5"/><path d="M4 4a12 12 0 0 0 0 14M22 4a12 12 0 0 1 0 14" fill="none" stroke="#8abf1e" stroke-width="2"/><rect x="12" y="7" width="2" height="6" fill="#8abf1e"/></svg></span>Risk Alerts<span class="chev"><svg width="10" height="7" viewBox="0 0 10 7"><path d="M1 1l4 4 4-4" fill="none" stroke="#fff" stroke-width="2"/></svg></span></div>
  <div class="abs col row" style="top:1091px"><span class="ic"><svg width="26" height="22" viewBox="0 0 26 22"><circle cx="13" cy="11" r="7" fill="none" stroke="#8abf1e" stroke-width="2.5"/><path d="M4 4a12 12 0 0 0 0 14M22 4a12 12 0 0 1 0 14" fill="none" stroke="#8abf1e" stroke-width="2"/><rect x="12" y="7" width="2" height="6" fill="#8abf1e"/></svg></span>Industry Alerts<span class="chev"><svg width="10" height="7" viewBox="0 0 10 7"><path d="M1 1l4 4 4-4" fill="none" stroke="#fff" stroke-width="2"/></svg></span></div>
  <div class="abs col row" style="top:1141px"><span class="ic"><svg width="26" height="22" viewBox="0 0 26 22"><circle cx="13" cy="11" r="7" fill="none" stroke="#8abf1e" stroke-width="2.5"/><path d="M4 4a12 12 0 0 0 0 14M22 4a12 12 0 0 1 0 14" fill="none" stroke="#8abf1e" stroke-width="2"/><rect x="12" y="7" width="2" height="6" fill="#8abf1e"/></svg></span>Business Alerts<span class="chev"><svg width="10" height="7" viewBox="0 0 10 7"><path d="M1 1l4 4 4-4" fill="none" stroke="#fff" stroke-width="2"/></svg></span></div>

  <!-- news map -->
  <div class="abs col bar" style="top:1196px">News articles from around the world<span class="chev"><svg width="10" height="7" viewBox="0 0 10 7"><path d="M1 6 5 2l4 4" fill="none" stroke="#fff" stroke-width="2"/></svg></span></div>
  <div class="abs col map" role="img" aria-label="Dotted world map showing where news articles were published" style="top:1262px;height:461px"></div>
  <svg class="abs" style="left:0;top:0" width="1170" height="1740" viewBox="0 0 1170 1740">
    <defs><g id="pin"><path d="M0 0c-9 0-15 7-15 15 0 11 15 22 15 22s15-11 15-22C15 7 9 0 0 0z"/><circle cy="14" r="6" fill="#fff"/></g></defs>
    <g fill="#3c8a2e">
      <use href="#pin" x="198" y="1380"/><use href="#pin" x="276" y="1465"/><use href="#pin" x="560" y="1515"/>
      <use href="#pin" x="647" y="1328"/><use href="#pin" x="773" y="1328"/><use href="#pin" x="790" y="1398"/><use href="#pin" x="543" y="1525" transform="translate(0,0)"/>
    </g>
    <g fill="#b6d531"><use href="#pin" x="380" y="1296"/><use href="#pin" x="331" y="1633"/><use href="#pin" x="881" y="1597"/><use href="#pin" x="478" y="1414"/></g>
  </svg>
  <div class="abs tip" style="left:525px;top:1310px;width:212px">NEWS<br>June 20, 2016<br>Lorem ipsum dolor sit amet, consectetuer adipiscing elit, sed diam nonummy.</div>
  <svg class="abs" style="left:500px;top:1400px" width="40" height="30" viewBox="0 0 40 30"><path d="M26 0 0 18 34 6z" fill="#b6d531"/></svg>
  <div class="abs year" style="left:500px;top:1744px;width:170px;height:34px">2016<svg width="14" height="9" viewBox="0 0 14 9"><path d="M1 1l6 6 6-6" fill="none" stroke="#444" stroke-width="2"/></svg></div>
  <div class="abs timeline" style="left:194px;top:1821px;width:790px"></div>
  <div class="abs dot" style="left:184px;top:1812px"></div><div class="abs dot" style="left:255px;top:1812px"></div><div class="abs dot" style="left:326px;top:1812px"></div><div class="abs dot" style="left:397px;top:1812px"></div><div class="abs dot" style="left:468px;top:1812px"></div><div class="abs dot on" style="left:539px;top:1812px"></div><div class="abs dot" style="left:610px;top:1812px"></div><div class="abs dot" style="left:681px;top:1812px"></div><div class="abs dot" style="left:752px;top:1812px"></div><div class="abs dot" style="left:823px;top:1812px"></div><div class="abs dot" style="left:894px;top:1812px"></div><div class="abs dot" style="left:965px;top:1812px"></div>
  <div class="abs month" style="left:164px;top:1856px">JAN</div><div class="abs month" style="left:235px;top:1856px">FEB</div><div class="abs month" style="left:306px;top:1856px">MAR</div><div class="abs month" style="left:377px;top:1856px">APR</div><div class="abs month" style="left:448px;top:1856px">MAY</div><div class="abs month on" style="left:519px">JUN</div><div class="abs month" style="left:590px;top:1856px">JUL</div><div class="abs month" style="left:661px;top:1856px">AUG</div><div class="abs month" style="left:732px;top:1856px">SEP</div><div class="abs month" style="left:803px;top:1856px">OCT</div><div class="abs month" style="left:874px;top:1856px">NOV</div><div class="abs month" style="left:945px;top:1856px">DEC</div>

  <!-- project status -->
  <div class="abs col bar" style="top:1899px">Project Status<span class="chev"><svg width="10" height="7" viewBox="0 0 10 7"><path d="M1 6 5 2l4 4" fill="none" stroke="#fff" stroke-width="2"/></svg></span></div>
  <div class="abs col panel" style="top:1959px;height:464px"></div>
  <div class="abs issue" style="left:170px;top:1992px;width:840px">
    <div style="position:absolute;left:0;top:0"><svg width="36" height="40" viewBox="0 0 22 24"><rect x="2" y="3" width="16" height="19" fill="none" stroke="#8abf1e" stroke-width="2"/><path d="M6 9h8M6 13h8M6 17h5" stroke="#8abf1e" stroke-width="1.6"/><circle cx="17" cy="19" r="4" fill="#8abf1e"/></svg></div>
    <div style="margin-left:50px"><h3>PROJECT A</h3>
      <p>Lorem ipsum dolor sit amet, consectetuer adipiscing elit, sed diam nonummy nibh euismod tincidunt ut laoreet dolore magna aliquam erat volutpat. Ut wisi enim ad minim veniam, quis nostrud exerci tation ullamcorper.</p></div>
  </div>
  <div class="abs" style="left:135px;top:2094px;width:900px;text-align:center;font-size:13px;font-weight:700;color:#444">COMPLETED PROCESS</div>
  <div class="abs circle" style="left:250px;top:2134px"><svg width="72" height="52" viewBox="0 0 72 52"><rect x="2" y="14" width="56" height="34" rx="3" fill="#a3cd3f"/><rect x="8" y="22" width="20" height="14" fill="#fff"/><path d="M12 27h12M12 31h8" stroke="#a3cd3f" stroke-width="2"/><path d="M34 38h18" stroke="#fff" stroke-width="3"/><path d="M66 2l4 4-26 26-7 3 3-7z" fill="#a3cd3f"/></svg></div>
  <div class="abs circle" style="left:521px;top:2134px"><svg width="74" height="48" viewBox="0 0 74 48"><g fill="#a3cd3f"><circle cx="37" cy="12" r="10"/><path d="M20 46c0-14 7-20 17-20s17 6 17 20z"/><circle cx="14" cy="17" r="7"/><path d="M0 44c0-10 5-14 14-14 3 0 5 1 7 2-3 3-4 7-4 12z"/><circle cx="60" cy="17" r="7"/><path d="M74 44c0-10-5-14-14-14-3 0-5 1-7 2 3 3 4 7 4 12z"/></g></svg></div>
  <div class="abs circle" style="left:792px;top:2134px"><svg width="76" height="66" viewBox="0 0 76 66"><g fill="#a3cd3f"><circle cx="14" cy="10" r="7"/><rect x="6" y="18" width="16" height="24" rx="3"/><circle cx="62" cy="30" r="7"/><rect x="54" y="38" width="16" height="24" rx="3"/><path d="M30 10h20l-4-5M50 10l-4 5" stroke="#a3cd3f" stroke-width="4" fill="none"/><path d="M46 56H26l4-5M26 56l4 5" stroke="#a3cd3f" stroke-width="4" fill="none"/></g></svg></div>
  <div class="abs cap" style="left:195px;top:2292px">Lorem ipsum dolor sit amet, consectetuer adipiscing elit, sed diam nonummy nibh.</div>
  <div class="abs cap" style="left:466px;top:2292px">Lorem ipsum dolor sit amet, consectetuer adipiscing elit, sed diam nonummy nibh.</div>
  <div class="abs cap" style="left:737px;top:2292px">Lorem ipsum dolor sit amet, consectetuer adipiscing elit, sed diam nonummy nibh.</div>
  <div class="abs btn" style="left:816px;top:2385px;width:219px;height:38px">Status : Data Analysing</div>

  <!-- budget -->
  <div class="abs col bar" style="top:2466px">Budget Overviews<span class="chev"><svg width="10" height="7" viewBox="0 0 10 7"><path d="M1 6 5 2l4 4" fill="none" stroke="#fff" stroke-width="2"/></svg></span></div>
  <div class="abs col row" style="top:2525px"><span class="ic"><svg width="26" height="26" viewBox="0 0 26 26"><g stroke="#8abf1e" stroke-width="3" stroke-linecap="round"><path d="M13 2v6M13 18v6M2 13h6M18 13h6M5 5l4 4M17 17l4 4M21 5l-4 4M9 17l-4 4"/></g></svg></span>Budget vs Cost<span class="chev"><svg width="10" height="7" viewBox="0 0 10 7"><path d="M1 6 5 2l4 4" fill="none" stroke="#fff" stroke-width="2"/></svg></span></div>
  <div class="abs col panel" style="top:2575px;height:194px"></div>
  <p class="abs copy" style="left:177px;top:2602px;width:820px">Lorem ipsum dolor sit amet, consectetuer adipiscing elit, sed diam nonummy nibh euismod tincidunt ut laoreet dolore magna aliquam erat volutpat. Ut wisi enim ad minim veniam, quis nostrud exerci tation ullamcorper sus cipit lobortis nisl ut aliquip ex ea commodo consequat. Duis autem vel eum iriure dolor in hendrerit in vulputate velit esse molestie consequat, vel illum dolore eu feugiat nulla facilisis at vero eros et accumsan.</p>
  <div class="abs btn" style="left:905px;top:2731px;width:130px;height:38px">View Details</div>
  <div class="abs col row" style="top:2771px"><span class="ic"><svg width="24" height="24" viewBox="0 0 24 24"><circle cx="12" cy="12" r="10" fill="none" stroke="#8abf1e" stroke-width="2.5"/><text x="12" y="17" text-anchor="middle" font-family="Open Sans,Arial,sans-serif" font-size="13" font-weight="700" fill="#8abf1e">$</text></svg></span>Planned vs Actual<span class="chev"><svg width="10" height="7" viewBox="0 0 10 7"><path d="M1 1l4 4 4-4" fill="none" stroke="#fff" stroke-width="2"/></svg></span></div>

</div>
</body>
</html>
```